Asian Pakistani: Wedding Invitation

Design a pakistani asian wedding invitation.
Islamic theme, with arabic text:

Text to be used:

Start with: bismillah and dua for marriage. (The Holy Quran chapter 25 verse 75 with arabic text and english translation below)

Mrs. Rukhsana Iqbal wife of (late) Mr. Nadeem Rauf Siddiqui
Cordially requests your company to grace the joyous occasion of the wedding of their beloved daughter
Sadia Siddiqui
Daughter of ( late) Mr Nadeem Rauf siddiqui
with
Imran Bashir
Son of Mr. Javed Bashir & Mrs Shaista Bashir

Insha’Allah on Thursday 29th August 2019 at Royal Orchid
12 Linden Crescent, Croydon
CR9 7TQ
Baraat Arrival 6:30

RSVP
Omar Siddiqui 07700 900412
Bilal Rehman 07700 900837
Shahzad Malik 07700 900265

Target Market(s)

Muslims

Font styles to use
Script

Colors

Designer to choose colors to be used in the design.

Requirements
Must have
• stylish calligraphy Arabic lettering of the dua requested above
• Size:
• Long 4" x 9.5"
Nice to have
• ottoman empire: Art theme

```html
<!DOCTYPE html>
<html lang="en">
<head>
<meta charset="utf-8">
<title>Wedding Invitation – Sadia &amp; Imran</title>
<link href="https://fonts.googleapis.com/css2?family=Aref+Ruqaa:wght@400;700&family=Yellowtail&family=Tinos:ital,wght@0,400;0,700;1,400&display=swap" rel="stylesheet">
<style>
  :root {
    --plum-top: #3b1747;
    --plum-mid: #4f1548;
    --wine-bottom: #72143f;
    --gold: #c9a46a;
    --gold-light: #e6cb98;
    --cream: #f4ecf2;
    --white: #ffffff;
    --pattern-navy: #2a1846;
    --ring-fill: #42174e;
  }
  * { margin: 0; padding: 0; box-sizing: border-box; }
  html, body { width: 1200px; height: 2850px; overflow: hidden; background: var(--pattern-navy); }
  .invitation { position: relative; width: 1200px; height: 2850px; overflow: hidden; }

  .side-pattern {
    position: absolute; top: 0; width: 138px; height: 2850px;
    background: linear-gradient(180deg, var(--pattern-navy), #3a1c4e 30%, var(--pattern-navy) 55%, #3b1a4a 80%, var(--pattern-navy));
  }
  .side-pattern::after {
    content: ""; position: absolute; inset: 0;
    background: linear-gradient(90deg, rgba(178,36,79,.25), rgba(201,164,106,.22), rgba(31,142,143,.2));
  }
  .side-pattern.left { left: 0; }
  .side-pattern.right { right: 0; }

  .panel {
    position: absolute; left: 127px; top: 0; width: 935px; height: 2850px;
    background: linear-gradient(180deg, var(--plum-top) 0%, var(--plum-mid) 55%, var(--wine-bottom) 100%);
    box-shadow: 0 0 30px rgba(0,0,0,.55);
    color: var(--cream); text-align: center;
    font-family: "Tinos", "Times New Roman", serif;
  }
  .mandala {
    position: absolute; left: 0; top: 0; width: 935px; height: 560px;
    background: radial-gradient(ellipse 470px 520px at 50% 0%, rgba(201,164,106,.55), rgba(120,70,80,.3) 60%, rgba(59,23,71,0) 100%);
  }

  .arabic { font-family: "Aref Ruqaa", "Amiri", serif; direction: rtl; }
  .bismillah {
    position: absolute; left: 0; top: 300px; width: 100%;
    font-size: 76px; line-height: 200px; font-weight: 700;
    color: var(--gold-light);
    text-shadow: 0 3px 10px rgba(40,10,40,.7);
  }

  .line { position: absolute; left: 0; width: 100%; white-space: nowrap; }
  .opening { top: 556px; font-size: 36px; color: var(--white); }

  .dua-ring {
    position: absolute; left: 91px; top: 645px; width: 755px; height: 755px;
    border-radius: 50%; border: 5px solid var(--gold);
    background: radial-gradient(circle, #4c1c57, var(--ring-fill));
    display: flex; align-items: center; justify-content: center;
  }
  .dua-text {
    font-size: 66px; line-height: 118px; font-weight: 700;
    color: var(--white);
  }

  .translation { top: 1428px; font-size: 31px; line-height: 40px; color: var(--cream); }
  .verse-ref { position: absolute; right: 20px; top: 1520px; font-size: 23px; font-style: italic; }

  .script { font-family: "Yellowtail", "Great Vibes", cursive; color: var(--white); }
  .host-name { top: 1592px; font-size: 60px; line-height: 64px; }
  .request { top: 1716px; font-size: 28px; line-height: 35px; }

  .flourish {
    position: absolute; left: 315px; width: 305px; height: 90px;
    background: radial-gradient(ellipse at center, rgba(201,164,106,.7), rgba(201,164,106,.15) 60%, rgba(0,0,0,0));
  }
  .flourish.upper { top: 1815px; }
  .flourish.lower { top: 2136px; }

  .couple-name { font-size: 92px; line-height: 100px; }
  .bride { top: 1908px; }
  .groom { top: 2200px; }
  .bride-parent { top: 2014px; font-size: 28px; }
  .with-word { top: 2090px; font-size: 36px; }
  .son-of { top: 2292px; font-size: 27px; }
  .groom-parents { top: 2328px; font-size: 60px; line-height: 66px; }
  .groom-parents .amp { font-family: "Tinos", serif; font-size: 40px; }

  .divider { position: absolute; left: 250px; width: 435px; height: 30px; }
  .divider.top { top: 2498px; }
  .divider.bottom { top: 2684px; }
  .event { top: 2548px; font-size: 28px; line-height: 36px; }
  .arrival { top: 2630px; font-size: 40px; }
  .arrival strong { font-weight: 700; }
  .rsvp-title { top: 2742px; font-size: 27px; }
  .rsvp-list { top: 2776px; font-size: 21px; }
  .rsvp-list span { margin: 0 13px; }
</style>
</head>
<body>
<div class="invitation">
  <div class="side-pattern left" role="img" aria-label="Ottoman floral damask pattern in navy, rose, teal and gold"></div>
  <div class="side-pattern right" role="img" aria-label="Ottoman floral damask pattern in navy, rose, teal and gold"></div>

  <main class="panel">
    <div class="mandala" role="img" aria-label="Gold ornamental mandala"></div>
    <p class="arabic bismillah" lang="ar">بِسْمِ ٱللَّٰهِ ٱلرَّحْمَٰنِ ٱلرَّحِيمِ</p>
    <p class="line opening">In The Name Of Allah, The Mostgracious, Most Merciful</p>

    <div class="dua-ring">
      <p class="arabic dua-text" lang="ar">رَبَّنَا هَبْ لَنَا مِنْ<br>أَزْوَاجِنَا وَذُرِّيَّاتِنَا<br>قُرَّةَ أَعْيُنٍ وَٱجْعَلْنَا<br>لِلْمُتَّقِينَ إِمَامًا</p>
    </div>

    <p class="line translation">Our Lord,&nbsp; Grant Us Of Our Wives And Childrenthe Delights<br>Of Our Eyes, And Make Us A Model Of The Righteous.</p>
    <p class="verse-ref">(Sura Al furqan: 75)</p>

    <p class="line script host-name">Mrs. Rukhsana Iqbal wife of (late)<br>Mr. Nadeem Rauf Siddiqui</p>
    <p class="line request">Cordially requests your company to grace the joyous occasion of the<br>wedding of their beloved daughter</p>

    <div class="flourish upper" role="img" aria-label="Gold floral flourish"></div>
    <p class="line script couple-name bride">Sadia Siddiqui</p>
    <p class="line bride-parent">Daughter of ( late) Mr Nadeem Rauf siddiqui</p>
    <p class="line with-word">with</p>
    <div class="flourish lower" role="img" aria-label="Gold floral flourish"></div>
    <p class="line script couple-name groom">Imran Bashir</p>
    <p class="line son-of">Son of</p>
    <p class="line script groom-parents">Mr. Javed Bashir <span class="amp">&amp;</span><br>Mrs Shaista Bashir</p>

    <svg class="divider top" viewBox="0 0 435 30" aria-hidden="true">
      <line x1="8" y1="15" x2="427" y2="15" stroke="#c9a46a" stroke-width="2"/>
      <circle cx="8" cy="15" r="4" fill="#c9a46a"/><circle cx="427" cy="15" r="4" fill="#c9a46a"/>
      <path d="M187 15 Q217 -2 247 15 Q217 32 187 15Z" fill="#c9a46a"/>
    </svg>
    <p class="line event">Insha’Allah on Thursday 29th August 2019 at<br>Royal Orchid 12 Linden Crescent, Croydon CR9 7TQ</p>
    <p class="line arrival">Baraat Arrival <strong>6:30 Pm</strong></p>
    <svg class="divider bottom" viewBox="0 0 435 30" aria-hidden="true">
      <line x1="8" y1="15" x2="427" y2="15" stroke="#c9a46a" stroke-width="2"/>
      <circle cx="8" cy="15" r="4" fill="#c9a46a"/><circle cx="427" cy="15" r="4" fill="#c9a46a"/>
      <path d="M187 15 Q217 -2 247 15 Q217 32 187 15Z" fill="#c9a46a"/>
    </svg>

    <p class="line rsvp-title">RSVP :</p>
    <p class="line rsvp-list"><span>Omar Siddiqui 07700 900412</span><span>Bilal Rehman 07700 900837</span><span>Shahzad Malik 07700 900265</span></p>
  </main>
</div>
</body>
</html>
```